Professional looking Roller Blind Discount Card that portrays quality at a value for money price!

We need a double sided business card designed as a discount card. Size 90mm wide x 55mm high.We would like it to look professional and portray quality at a value for money price point.I have uploaded a word document with a basic layout with the information we want included on each side of the card. Please put your own thought into the layout.

Contact Information for Business Card

As per word document attached.

```html
<!DOCTYPE html>
<html lang="en">
<head>
<meta charset="utf-8">
<title>Roller Blinds Discount Card</title>
<link href="https://fonts.googleapis.com/css2?family=Open+Sans:wght@400;600;700;800&display=swap" rel="stylesheet">
<style>
  :root {
    --stage: #2b2b2d;
    --card: #141414;
    --card-edge: #1f1f21;
    --blue: #5aa8e6;
    --blue-deep: #2f7fbf;
    --grey: #a9a9ad;
    --gold: #d9a93a;
    --gold-light: #f7e08a;
    --gold-dark: #9c6d14;
    --white: #f2f2f2;
    --photo-a: #3a3b3e;
    --photo-b: #505257;
  }
  * { margin: 0; padding: 0; box-sizing: border-box; }
  html, body { width: 1200px; height: 1101px; overflow: hidden; }
  body {
    background: var(--stage);
    font-family: "Open Sans", Arial, sans-serif;
    position: relative;
  }
  .card {
    position: absolute;
    left: 200px;
    width: 800px;
    height: 489px;
    background: linear-gradient(160deg, var(--card-edge), var(--card) 55%, #0d0d0d);
    border-radius: 4px;
    box-shadow: 0 10px 30px rgba(0,0,0,.45);
    overflow: hidden;
  }
  .card--front { top: 40px; }
  .card--back { top: 572px; }

  .front__title {
    position: absolute; top: 22px; left: 0; right: 0;
    text-align: center;
    color: var(--blue);
    font-weight: 700; font-size: 62px; letter-spacing: 9px;
    line-height: 1;
  }
  .rule-row {
    position: absolute; left: 40px; right: 40px;
    display: flex; align-items: center; gap: 14px;
  }
  .rule-row::before, .rule-row::after {
    content: ""; flex: 1; height: 2px;
    background: linear-gradient(90deg, var(--gold-dark), var(--gold-light), var(--gold-dark));
  }
  .front__tagline { top: 98px; }
  .front__tagline span { color: var(--grey); font-weight: 700; font-size: 23px; white-space: nowrap; }

  .front__photo {
    position: absolute; left: 40px; right: 40px; top: 140px; height: 225px;
    border: 3px solid var(--blue);
    background: linear-gradient(180deg, var(--photo-b), var(--photo-a));
  }
  .front__brand {
    position: absolute; right: 44px; top: 372px;
    display: flex; align-items: center; gap: 10px;
    color: var(--white); font-weight: 600; font-size: 26px; letter-spacing: 1px;
  }
  .front__brand i { width: 18px; height: 18px; background: var(--blue); display: block; }

  .call { bottom: 30px; }
  .call span { font-size: 36px; color: var(--grey); white-space: nowrap; }
  .call b { color: var(--blue); font-weight: 700; }

  .back__offer {
    position: absolute; top: 18px; left: 0; right: 0; text-align: center;
    color: var(--blue); font-weight: 800; font-size: 76px; letter-spacing: 4px; line-height: 1;
  }
  .back__lines {
    position: absolute; top: 108px; left: 0; right: 0; text-align: center;
    color: var(--grey); font-weight: 700; font-size: 27px; line-height: 1.3;
  }
  .badges {
    position: absolute; top: 200px; left: 60px; right: 60px;
    display: flex; justify-content: space-between;
  }
  .badge { position: relative; width: 180px; height: 180px; }
  .badge svg { position: absolute; inset: 0; }
  .badge__text {
    position: absolute; inset: 0;
    display: flex; align-items: center; justify-content: center; text-align: center;
    color: var(--gold-light); font-weight: 800; font-size: 21px; line-height: 1.05;
    text-shadow: 0 2px 2px rgba(0,0,0,.55);
  }
  .badge__text em { font-style: normal; font-size: 30px; }
</style>
</head>
<body>
  <svg width="0" height="0" style="position:absolute">
    <defs>
      <linearGradient id="goldRing" x1="0" y1="0" x2="1" y2="1">
        <stop offset="0" stop-color="#fbe9a0"/>
        <stop offset=".45" stop-color="#d9a93a"/>
        <stop offset=".7" stop-color="#f3d47a"/>
        <stop offset="1" stop-color="#9c6d14"/>
      </linearGradient>
      <radialGradient id="blueCore" cx=".45" cy=".35" r=".7">
        <stop offset="0" stop-color="#6fc0ee"/>
        <stop offset="1" stop-color="#1f6ea8"/>
      </radialGradient>
      <symbol id="seal" viewBox="0 0 180 180">
        <circle cx="90" cy="90" r="86" fill="url(#goldRing)"/>
        <circle cx="90" cy="90" r="70" fill="#b8861f"/>
        <circle cx="90" cy="90" r="64" fill="url(#blueCore)"/>
      </symbol>
    </defs>
  </svg>

  <section class="card card--front">
    <h1 class="front__title">ROLLER BLINDS</h1>
    <div class="rule-row front__tagline"><span>FREE in Home Measure &amp; Quote</span></div>
    <div class="front__photo" role="img" aria-label="Photo of coloured roller blind fabric rolls beside a bright room with fitted blinds"></div>
    <div class="front__brand"><i></i>K&amp;M INTERIORS</div>
    <div class="rule-row call"><span>Call <b>0491 570 006</b> Today</span></div>
  </section>

  <section class="card card--back">
    <h2 class="back__offer">25% OFF</h2>
    <p class="back__lines">Quality Custom Made Roller Blinds<br>Blockout – Screen – Light Filtering</p>
    <div class="badges">
      <div class="badge"><svg viewBox="0 0 180 180"><use href="#seal"/></svg><div class="badge__text"><span><em>FREE</em><br>in Home<br>Measure &amp;<br>Quote</span></div></div>
      <div class="badge"><svg viewBox="0 0 180 180"><use href="#seal"/></svg><div class="badge__text"><span>Best Price<br>Guarantee</span></div></div>
      <div class="badge"><svg viewBox="0 0 180 180"><use href="#seal"/></svg><div class="badge__text"><span>Family<br>Owned &amp;<br>Operated</span></div></div>
    </div>
    <div class="rule-row call"><span>Call <b>0491 570 006</b> Today</span></div>
  </section>
</body>
</html>
```